Accounting business needs business card

I have a business card but need something better. I want the colour changed and the design to be better. I have uploaded a picture of my new sign that is grey in colour, i would like to incorporate these colours.

```html
<!DOCTYPE html>
<html lang="en">
<head>
<meta charset="utf-8">
<title>Level Ledger – Business Card</title>
<link rel="stylesheet" href="https://fonts.googleapis.com/css2?family=Poppins:wght@300;400;600;700&display=swap">
<style>
  :root {
    --page-bg: #2b2f36;
    --silver-light: #f1f2f3;
    --silver-mid: #d6d8da;
    --silver-dark: #b9bcbf;
    --ink: #2a2c2e;
    --ink-soft: #4a4d50;
    --slate-dark: #152426;
    --slate-mid: #1f3336;
    --steel-text: #c9ced0;
    --plain-badge: #9ea2a6;
  }
  * { margin: 0; padding: 0; box-sizing: border-box; }
  html, body { width: 1200px; height: 900px; overflow: hidden; }
  body {
    background: var(--page-bg);
    font-family: "Poppins", sans-serif;
    position: relative;
  }
  .card {
    position: absolute;
    top: 290px;
    width: 540px;
    height: 310px;
    border-radius: 4px;
    box-shadow: 0 12px 30px rgba(0,0,0,.45);
    overflow: hidden;
  }
  .card-front {
    left: 45px;
    background:
      repeating-linear-gradient(0deg, rgba(255,255,255,.18) 0 1px, rgba(0,0,0,.03) 1px 3px),
      linear-gradient(120deg, var(--silver-light), var(--silver-mid) 55%, var(--silver-dark));
    color: var(--ink);
  }
  .brand {
    position: absolute; left: 28px; top: 34px;
    display: flex; align-items: center; gap: 14px;
  }
  .brand-mark {
    width: 40px; height: 40px; border-radius: 50%;
    border: 2px solid var(--ink);
  }
  .brand-name {
    font-size: 19px; font-weight: 400; letter-spacing: 7px;
    color: var(--ink);
  }
  .front-divider {
    position: absolute; left: 28px; top: 112px; width: 210px; height: 1px;
    background: var(--ink-soft);
  }
  .membership {
    position: absolute; left: 28px; top: 140px;
    display: flex; align-items: center; gap: 12px;
  }
  .member-badge {
    width: 100px; height: 46px;
    background: var(--plain-badge);
  }
  .member-note { font-size: 10px; line-height: 1.35; color: var(--ink-soft); width: 100px; }
  .partner {
    position: absolute; left: 28px; top: 222px;
    display: flex; align-items: center; gap: 8px;
  }
  .partner-dot { width: 30px; height: 30px; border-radius: 50%; background: var(--plain-badge); }
  .partner-name { font-size: 15px; font-weight: 400; color: var(--ink); }

  .person {
    position: absolute; right: 28px; top: 34px; width: 250px; text-align: right;
  }
  .person-name { font-size: 19px; font-weight: 700; letter-spacing: .5px; }
  .person-creds { font-size: 11px; font-weight: 400; margin-top: 2px; }
  .person-title { font-size: 11px; font-weight: 300; margin-top: 1px; }
  .person-rule { width: 22px; height: 2px; background: var(--ink); margin: 12px 0 12px auto; }
  .contact-list { list-style: none; }
  .contact-list li {
    display: flex; justify-content: flex-end; align-items: center; gap: 8px;
    font-size: 11.5px; line-height: 20px;
  }
  .contact-icon {
    width: 15px; height: 15px; border-radius: 50%; background: var(--ink);
    display: flex; align-items: center; justify-content: center;
  }
  .contact-icon svg { width: 9px; height: 9px; }
  .contact-rule { width: 160px; height: 1px; background: var(--ink-soft); margin: 10px 0 10px auto; }
  .agent {
    display: flex; justify-content: flex-end; align-items: center; gap: 10px;
  }
  .agent-seal {
    width: 40px; height: 40px; border-radius: 50%;
    background: var(--plain-badge);
  }
  .agent-text { font-size: 11px; line-height: 1.2; text-align: left; }

  .card-back {
    left: 615px;
    background:
      repeating-linear-gradient(0deg, rgba(255,255,255,.025) 0 1px, rgba(0,0,0,.05) 1px 3px),
      linear-gradient(135deg, var(--slate-mid), var(--slate-dark));
  }
  .back-brand {
    position: absolute; left: 0; right: 0; top: 118px;
    display: flex; justify-content: center; align-items: center; gap: 16px;
  }
  .back-brand .brand-mark { border-color: var(--steel-text); width: 48px; height: 48px; }
  .back-brand .brand-name { color: var(--steel-text); font-size: 22px; letter-spacing: 9px; }
  .social {
    position: absolute; right: 22px; bottom: 20px; display: flex; gap: 5px;
  }
  .social span {
    width: 18px; height: 18px; border-radius: 50%;
    border: 1.5px solid var(--steel-text);
  }
</style>
</head>
<body>

<section class="card card-front" aria-label="Business card front">
  <div class="brand">
    <span class="brand-mark"></span>
    <span class="brand-name">LEVEL LEDGER</span>
  </div>
  <div class="front-divider"></div>

  <div class="membership">
    <span class="member-badge" role="img" aria-label="Professional body membership badge"></span>
    <p class="member-note">Level Ledger is an accredited practice</p>
  </div>

  <div class="partner">
    <span class="partner-dot"></span>
    <span class="partner-name">Ledgra</span>
  </div>

  <div class="person">
    <h1 class="person-name">OWEN HARTLEY</h1>
    <p class="person-creds">CPA, MTAX, BCOM (Acc &amp; Fin)</p>
    <p class="person-title">Taxation and Business Accountant</p>
    <div class="person-rule"></div>
    <ul class="contact-list">
      <li>0400 555 018
        <span class="contact-icon"><svg viewBox="0 0 10 10"><path d="M2 1.2 3.6 1l.8 2-1 .8a5 5 0 0 0 2.8 2.8l.8-1 2 .8L8.8 8C5 8.5 1.5 5 2 1.2z" fill="#fff"/></svg></span>
      </li>
      <li>owen@levelledger.com.au
        <span class="contact-icon"><svg viewBox="0 0 10 10"><rect x="1" y="2.5" width="8" height="5" fill="none" stroke="#fff"/><path d="M1 2.5 5 5.5 9 2.5" fill="none" stroke="#fff"/></svg></span>
      </li>
      <li>www.levelledger.com.au
        <span class="contact-icon"><svg viewBox="0 0 10 10"><circle cx="5" cy="5" r="3.8" fill="none" stroke="#fff"/><ellipse cx="5" cy="5" rx="1.6" ry="3.8" fill="none" stroke="#fff"/><path d="M1.2 5h7.6" stroke="#fff"/></svg></span>
      </li>
    </ul>
    <div class="contact-rule"></div>
    <div class="agent">
      <span class="agent-seal" role="img" aria-label="Registered tax agent seal"></span>
      <p class="agent-text">Tax agent<br>10293847</p>
    </div>
  </div>
</section>

<section class="card card-back" aria-label="Business card back">
  <div class="back-brand">
    <span class="brand-mark"></span>
    <span class="brand-name">LEVEL LEDGER</span>
  </div>
  <div class="social" aria-label="Social media links">
    <span></span><span></span><span></span>
  </div>
</section>

</body>
</html>
```